Clinical Hypnotherapy

I need a flyer to promote my services as a highly qualified Clinical Hypnotherapist . This flyer will be distributed at various alternative health clinic where I see clients and should explain to the client what hypnotherapy is and how it can help them . I would like it to match my website ( www.brentmoorcalm.co.uk ) as closely as possible in terms of the images , fonts and colours used . For this reason I include the following information that was supplied by the web designers :
Image : www.pixaloom.com - photo no. 4817264
Fonts in banner : Avenir Next Condensed , Arial Narrow
Main colour used for background : #0b3166
Attached is a file with text . Depending on available space I can provide additional text or if neccesary remove text .
Kindly also inform me of the cost prior to going ahead
Updates
Thank you for designs submitted so far . My fault but I realise that I originally included way too much text in my brief . Please find new attachment with reduced text . This will hopefully allow for a more eye catching less cluttered design . I would also like to have a logo designed for Brentmoor Calm - something abstract which reflects the psychotherapeutic / mind nature of the therapy .
Industry/Entity Type
Hypnotherapy
Look and feel
Each slider illustrates characteristics of the customer's brand and the style your logo design should communicate.

```html
<!DOCTYPE html>
<html lang="en">
<head>
<meta charset="utf-8">
<title>Brentmoor Calm – Clinical Hypnotherapy Flyer</title>
<link href="https://fonts.googleapis.com/css2?family=Arimo:ital,wght@0,400;0,700;1,700&family=Archivo+Narrow:wght@400;600&display=swap" rel="stylesheet">
<style>
:root{
  --navy:#0b3166;
  --navy-deep:#082650;
  --ink:#2b2b2b;
  --muted:#555;
  --strip:#e3e7ee;
  --box:#dfe4ec;
  --bg:#e9eaec;
  --white:#fff;
}
*{margin:0;padding:0;box-sizing:border-box}
html,body{width:1200px;height:1000px;overflow:hidden;background:var(--bg)}
body{font-family:"Arimo",Arial,sans-serif;color:var(--ink);position:relative}
.flyer{position:absolute;top:115px;width:545px;height:770px;background:var(--white);overflow:hidden;box-shadow:0 2px 8px rgba(0,0,0,.18)}
.flyer--front{left:40px}
.flyer--back{left:615px}
.banner{position:absolute;left:0;top:0;width:100%;height:210px;background:linear-gradient(180deg,#123d78,var(--navy))}
.portrait-frame{position:absolute;left:33px;top:33px;width:152px;height:232px;background:var(--white);padding:6px;box-shadow:0 1px 4px rgba(0,0,0,.3);z-index:2}
.portrait{width:100%;height:100%;background:linear-gradient(180deg,#1a1a1c 0%,#2c2f36 55%,#3b3f48 100%)}
.quote{position:absolute;left:222px;top:60px;width:300px;font-family:"Archivo Narrow","Arial Narrow",sans-serif;font-size:20.5px;line-height:26px;color:var(--white)}
.name-strip{position:absolute;left:0;top:210px;width:100%;height:52px;background:linear-gradient(90deg,var(--strip) 0%,#f3f5f8 70%,var(--white) 100%)}
.name{position:absolute;left:215px;top:232px;z-index:3}
.name strong{display:block;font-size:13.5px;color:var(--navy)}
.name span{display:block;font-size:11px;color:var(--navy);margin-top:1px}
.col{position:absolute;top:290px}
.about{left:32px;width:214px}
.about h2{font-weight:400;font-size:15.5px;color:var(--navy);line-height:16px}
.about p{font-size:8.6px;line-height:10.6px;color:var(--muted);margin-bottom:6px}
.side{left:265px;width:255px;border-left:1px dashed #999;padding-left:14px;height:350px}
.box-head{display:inline-block;background:linear-gradient(90deg,var(--box),rgba(223,228,236,0));color:var(--navy);font-size:13.5px;padding:5px 40px 5px 6px;margin-bottom:10px}
.bullets{list-style:none;font-size:10.2px;color:#333}
.bullets li{line-height:18.5px}
.bullets li::before{content:"• "}
.two-up{display:grid;grid-template-columns:108px 1fr}
.gap{height:18px}
.footer{position:absolute;left:0;bottom:0;width:100%;height:102px;background:var(--navy)}
.badge{position:absolute;left:27px;top:0;width:78px;height:102px;background:var(--white)}
.badge svg{position:absolute;left:9px;top:21px}
.call{position:absolute;left:118px;top:30px;font-size:10px;line-height:14px;color:var(--white)}
.call b{font-size:13px}
.more{position:absolute;left:350px;top:35px;border-left:1px solid var(--white);padding-left:10px;font-size:10px;line-height:14px;color:var(--white)}
.back-left{left:32px;width:215px}
.back-left .box-head{font-size:17px;padding:6px 40px 6px 10px}
.back-left p{font-size:10.2px;line-height:12.8px;color:#333}
.fact{font-weight:700;font-style:italic;color:var(--navy);font-size:11px !important;margin-top:8px}
.back-right{left:266px;top:290px;width:255px;border-left:1px dashed #999;padding-left:14px;height:355px}
.symptoms{list-style:none;font-size:9.8px;color:#333}
.symptoms li{line-height:17.4px}
.rule{border-top:1px dotted #999;margin:12px 0 18px}
.back-right p{font-size:10.2px;line-height:14.5px;color:#333}
</style>
</head>
<body>

<section class="flyer flyer--front">
  <div class="banner"></div>
  <div class="portrait-frame"><div class="portrait" role="img" aria-label="Portrait photo of the hypnotherapist in a dark suit"></div></div>
  <p class="quote">“Are YOU struggling with problems made worse by STRESS and ANXIETY or do you just need to make a CHANGE in your life?”</p>
  <div class="name-strip"></div>
  <div class="name"><strong>Daniel Ashcombe</strong><span>PgDip (Clin.Hyp.) PDCHyp.PDCBHyp, MWSH</span></div>

  <div class="col about">
    <h2>ABOUT ME</h2>
    <p>I am a certified and accredited Clinical Hypnotherapist with a Post Graduate Certificate in Clinical Hypnotherapy from the Westbridge College of Clinical Hypnosis (WCCH) in association with the University of Harlowmere (UH). I see clients at my clinic in Brentmoor, The Stillwater Therapy Centre in Eastcombe and The Orrin Clinic in Kettlewick.</p>
    <p>After a successful career as a performer, my interest in hypnotherapy developed from personal experience of hypnosis as well as other forms of trance-work and healing. I am convinced in its ability to transform lives and empower individuals. In recent years scientific research has resulted in a greater understanding of the subconscious mind and how it works.</p>
    <p>Hypnotherapy is neither mystical nor magical but can help effect extraordinary, and often rapid change in peoples’ lives, by helping to change subconscious beliefs, habits and associations. Hypnotherapy is a solution-focussed approach which provides you with the tools and resources to take control of your life, improve self-esteem and develop self-confidence.</p>
    <p>I work with a wide range of conditions but have come to specialise in weight loss and eating disorders as well as anxiety and stress-related conditions. I make use of an eclectic range of techniques, including Clinical Hypnosis, Cognitive Behavioural Hypnosis (CBH), Mindfulness, Eye Movement Desensitization and Reprocessing (EMDR) and Ego State Therapy, in order to tailor therapy to your unique needs and to help achieve a positive outcome.</p>
  </div>

  <div class="col side">
    <div class="box-head">Hypnosis Can Help You...</div>
    <ul class="bullets">
      <li>Manage stress</li>
      <li>Resolve emotional blocks</li>
      <li style="line-height:13px;margin:3px 0">Adapt unhelpful beliefs and<br>&nbsp;&nbsp;behaviours to become beneficial ones</li>
      <li>Develop greater self-esteem</li>
      <li>Create emotional and practical resources</li>
      <li>Establish positive new goals for the future</li>
    </ul>
    <div class="gap"></div>
    <div class="box-head">Clinical Hypnotherapy Can Help You With:</div>
    <ul class="bullets two-up">
      <li>Addictions</li><li>Pain Management</li>
      <li>Weight Control</li><li>Panic Attacks</li>
      <li>Anxiety</li><li>Performance Anxiety</li>
      <li>Binge Eating</li><li>Phobias</li>
      <li>Depression</li><li>Sleep Problems/ Insomnia</li>
      <li>Low Self Esteem</li><li>Sports Performance</li>
      <li>Stop Smoking</li><li>Cancer Support</li>
      <li>Managing Stress</li><li>Virtual Gastric Band</li>
    </ul>
  </div>

  <footer class="footer">
    <div class="badge"><svg width="60" height="60" viewBox="0 0 60 60"><circle cx="30" cy="30" r="28" fill="none" stroke="#222" stroke-width="2"/></svg></div>
    <p class="call">Why not call me on <b>075 2186 4390</b> or<br>email me at <b>daniel@brentmoorcalm.co.uk</b><br>for a quick, friendly, no-obligation consultation.</p>
    <p class="more">More informationcan be found at<br><b>www.brentmoorcalm.co.uk</b></p>
  </footer>
</section>

<section class="flyer flyer--back">
  <div class="banner"></div>
  <div class="portrait-frame"><div class="portrait" role="img" aria-label="Portrait photo of the hypnotherapist in a dark suit"></div></div>
  <p class="quote">“Are YOU struggling with problems made worse by STRESS and ANXIETY or do you just need to make a CHANGE in your life?”</p>
  <div class="name-strip"></div>
  <div class="name"><strong>Daniel Ashcombe</strong><span>PgDip (Clin.Hyp.) PDCHyp.PDCBHyp, MWSH</span></div>

  <div class="col back-left">
    <div class="box-head">HYPNOSIS</div>
    <p>Hypnosis is a state of deep relaxation during which one can act on appropriate suggestions made by the therapist. Hypnosis is not sleep but a trance-like state. In hypnosis the client remains in control at all times and cannot be made to do anything they do not want to do. One of the positive effects of hypnosis is the deep state of relaxation which we experience and whichturns down our sympathetic nervous system’s response to stress; slowing our heart-rate, lowering our blood pressure and improving our digestion amongst other things.</p>
    <p class="fact">It’s a fact that you cannot be both relaxed and stressed simultaneously</p>
    <div style="height:26px"></div>
    <div class="box-head">STRESS AND ANXIETY</div>
    <p>Everyone is affected by stress in different ways but these are some of the symptoms you may be experiencing:</p>
  </div>

  <div class="col back-right">
    <ul class="symptoms">
      <li>• Inability to relax • Increased heart rate</li>
      <li>• Irritability • Change in eating habits</li>
      <li>• Digestive problems • Feeling ‘down’</li>
      <li>• Forgetfulness • Aches and pains</li>
      <li>• Headaches • Sleep problems</li>
      <li>• Poor concentration</li>
      <li>• Destructive behaviour e.g. excessive drinking</li>
    </ul>
    <div class="rule"></div>
    <p>Hypnosis is very effective in helping to counteract the effects of stress since many hypnotic techniques utilise relaxation. In the hypnotic state the heart rate and metabolic rate slows and blood pressure decreases. The simple fact is that your body cannot be both relaxed and stressed simultaneously. If you pair a negative stress stimulus with relaxation, the dominant emotion will replace the weaker one. Teaching you how to practise self-hypnosis will help you access and experience the benefits of this state of deep relaxation</p>
  </div>

  <footer class="footer">
    <div class="badge"><svg width="60" height="60" viewBox="0 0 60 60"><circle cx="30" cy="30" r="28" fill="none" stroke="#222" stroke-width="2"/></svg></div>
    <p class="call">Why not call me on <b>075 2186 4390</b> or<br>email me at <b>daniel@brentmoorcalm.co.uk</b><br>for a quick, friendly, no-obligation consultation.</p>
    <p class="more">More informationcan be found at<br><b>www.brentmoorcalm.co.uk</b></p>
  </footer>
</section>

</body>
</html>
```